Design my dad a new business card because his current one sucks!

I need a business card designed for my fathers home maintenance business. His customers are individuals (single moms, old people etc.) as well as the occasional business. As such it needs to be accessible to both target audiences.

The front of the card should be dark grey on yellow with the logo and contain the following information:
- Darren Whitlock
- 0488 372 915
- info@bluegumhomecare.example.au
- 0488 372 915

- ABN: 71 284 630 912
- 'Fully Insured'

The reverse should be yellow on dark grey and will have the web address:
- bluegumhomecare.example.au

And a few key services he offers:
GENERAL REPAIRS
PAINTING/TILING/
PAVING &CONCRETING
PRESSURE WASHING
ON-SITE WELDING
DECKING ADDITIONS & REPAIRS
FENCING
FULL BOND CLEANING

This will be first time the logo has been printed so you will need to come up with the best CMYK approximation of the RGB colours to make sure it is a close as possible.

```html
<!DOCTYPE html>
<html lang="en">
<head>
<meta charset="utf-8">
<title>Bluegum Home Care – Business Card</title>
<link rel="stylesheet" href="https://fonts.googleapis.com/css2?family=Ubuntu:wght@400;500;700&display=swap">
<style>
  :root {
    --card-yellow: #efc51c;
    --card-charcoal: #2d2926;
    --ink-dark: #2a2622;
    --page-bg: #e4e4e2;
  }
  * { margin: 0; padding: 0; box-sizing: border-box; }
  html, body {
    width: 1200px;
    height: 1000px;
    overflow: hidden;
    background: var(--page-bg);
    font-family: "Ubuntu", Arial, sans-serif;
  }
  .canvas {
    position: relative;
    width: 1200px;
    height: 1000px;
  }
  .card {
    position: absolute;
    left: 230px;
    width: 740px;
    height: 420px;
    box-shadow: 0 6px 18px rgba(0,0,0,0.18);
  }
  .card-front { top: 60px; background: var(--card-yellow); color: var(--ink-dark); }
  .card-back  { top: 520px; background: var(--card-charcoal); color: var(--card-yellow); }

  .card-frame {
    position: absolute;
    inset: 18px;
    border: 1.5px solid currentColor;
  }

  /* brand wordmark */
  .brand {
    position: absolute;
    display: flex;
    align-items: center;
    gap: 12px;
    font-weight: 700;
    letter-spacing: 1px;
    text-transform: uppercase;
    white-space: nowrap;
  }
  .brand-dot {
    width: 34px;
    height: 34px;
    border-radius: 50%;
    background: currentColor;
    flex: none;
  }
  .card-front .brand { top: 62px; left: 200px; font-size: 36px; }
  .card-back .brand { top: 58px; left: 212px; font-size: 30px; }
  .card-back .brand-dot { width: 28px; height: 28px; }

  .rule {
    position: absolute;
    height: 2px;
    background: currentColor;
  }
  .card-front .rule { top: 132px; left: 60px; width: 560px; }

  /* front contact block */
  .contact {
    position: absolute;
    top: 196px;
    left: 48px;
    font-size: 21px;
    line-height: 1.4;
  }
  .contact-name {
    font-size: 22px;
    font-weight: 700;
    text-transform: uppercase;
    border-bottom: 2px solid currentColor;
    display: inline-block;
    padding-bottom: 1px;
    margin-bottom: 4px;
    letter-spacing: 0.5px;
  }
  .contact-line {
    display: flex;
    align-items: center;
    gap: 8px;
  }
  .contact-icon { width: 20px; height: 20px; flex: none; }
  .abn {
    position: absolute;
    top: 335px;
    left: 230px;
    font-size: 21px;
    letter-spacing: 0.3px;
  }

  /* back */
  .web-address {
    position: absolute;
    top: 108px;
    left: 0;
    width: 100%;
    text-align: center;
    font-size: 19px;
  }
  .card-back .rule { top: 140px; left: 110px; width: 520px; }
  .services {
    position: absolute;
    top: 152px;
    left: 0;
    width: 100%;
    list-style: none;
    text-align: center;
    font-size: 20px;
    line-height: 1.2;
    text-transform: uppercase;
    letter-spacing: 0.5px;
  }
</style>
</head>
<body>
<main class="canvas">

  <section class="card card-front" aria-label="Business card front">
    <div class="card-frame"></div>
    <div class="brand"><span class="brand-dot"></span>Bluegum Home Care</div>
    <div class="rule"></div>
    <div class="contact">
      <div class="contact-name">Darren Whitlock</div>
      <div class="contact-line">
        <svg class="contact-icon" viewBox="0 0 20 20" aria-hidden="true">
          <circle cx="10" cy="10" r="10" fill="var(--ink-dark)"/>
          <path d="M6.3 5.2c.4-.3.9-.3 1.2.1l1.2 1.6c.3.4.2.9-.1 1.2l-.7.6c.6 1.3 1.5 2.3 2.8 2.9l.6-.7c.3-.4.8-.4 1.2-.1l1.6 1.2c.4.3.4.8.1 1.2l-.8.9c-.5.5-1.3.7-2 .4-2.7-1.1-4.7-3.1-5.8-5.8-.3-.7-.1-1.5.4-2z" fill="var(--card-yellow)"/>
        </svg>
        <span>0488 372 915</span>
      </div>
      <div class="contact-line">
        <svg class="contact-icon" viewBox="0 0 20 20" aria-hidden="true">
          <circle cx="10" cy="10" r="10" fill="var(--ink-dark)"/>
          <rect x="5" y="6.5" width="10" height="7" rx="0.8" fill="var(--card-yellow)"/>
          <path d="M5.3 7l4.7 3.6L14.7 7" fill="none" stroke="var(--ink-dark)" stroke-width="1"/>
        </svg>
        <span>info@bluegumhomecare.example.au &nbsp;- &nbsp;'Fully Insured'</span>
      </div>
    </div>
    <div class="abn">ABN: 71 284 630 912</div>
  </section>

  <section class="card card-back" aria-label="Business card back">
    <div class="card-frame"></div>
    <div class="brand"><span class="brand-dot"></span>Bluegum Home Care</div>
    <div class="web-address">bluegumhomecare.example.au</div>
    <div class="rule"></div>
    <ul class="services">
      <li>General Repairs</li>
      <li>Painting/Tiling/</li>
      <li>Paving &amp;Concreting</li>
      <li>Pressure Washing</li>
      <li>On-Site Welding</li>
      <li>Decking Additions &amp; Repairs</li>
      <li>Fencing</li>
      <li>Full Bond Cleaning</li>
    </ul>
  </section>

</main>
</body>
</html>
```